'The Wattlebrook' @2847 Silverfern Crescent Road, Greenwith

Hi, We need a For Sale brochure done for a new land division. I work in Real Estate and have have listed 14 Land Allotments and would like a nice brochure done.

The land is near some green hills and the site use to be called the Kennel Haven. I thought the development could be called 'The Wattlebrook' 14 Premium Allotments Greenwith.

The design we would like the name of the development across the front. Some hills, or sunset, something to represent lifestyle living.

Write Up:
Premium 14 Allotments For Sale
Blocks 359m2 - 496m2

The Wattlebrook offers; Sunning view to the hills, convenient location to local shops, transport and schools.

Build your dream home in this premium location on the ideal sized allotment.

Be apart of something special The Wattlebrook Allotments will sell quickly only 14 Available

Target Market(s)

Property Buyers looking to build their dream home on a nice block of land

Industry/Entity Type

Real Estate

Colors
add136

Requirements
Must have
• Logo, Address, Some Hills, Our company details and logo,
Nice to have
• Green Hills or sunset. Professional brochure.

```html
<!DOCTYPE html>
<html lang="en">
<head>
<meta charset="utf-8">
<title>The Wattlebrook – 14 Premium Allotments Greenwith</title>
<link rel="stylesheet" href="https://fonts.googleapis.com/css2?family=Lato:wght@300;400;700&family=Montserrat:wght@700&family=Didact+Gothic&display=swap">
<style>
  :root {
    --green: #add136;
    --green-deep: #8fb82a;
    --orange: #f28c1e;
    --ink: #4a4a4a;
    --ink-soft: #666;
    --paper: #ffffff;
    --fold-shade: #f1f1f1;
    --stage-top: #d0d0d0;
    --stage-bottom: #ececec;
    --band-grey: #dcdcdc;
  }
  * { box-sizing: border-box; margin: 0; padding: 0; }
  html, body { width: 1200px; height: 982px; overflow: hidden; }
  body {
    background: linear-gradient(180deg, var(--stage-top), var(--stage-bottom));
    font-family: "Lato", sans-serif;
    color: var(--ink);
  }
  .brochure {
    position: absolute;
    left: 90px; top: 110px;
    width: 1020px; height: 760px;
    display: flex;
    box-shadow: 0 18px 40px rgba(0,0,0,.18);
  }
  .panel {
    position: relative;
    width: 340px; height: 100%;
    background: var(--paper);
    overflow: hidden;
  }
  .panel + .panel { border-left: 1px solid #e4e4e4; }
  .panel--contact { background: linear-gradient(90deg, var(--paper), var(--fold-shade)); }

  .photo { position: absolute; left: 0; top: 0; width: 100%; }
  .photo--entrance {
    height: 300px;
    background: linear-gradient(180deg, #b9cfa0 0%, #6f8f4a 45%, #8a8478 75%, #6f6a60 100%);
  }
  .photo--meadow {
    height: 360px;
    background: radial-gradient(circle at 75% 25%, #e9d48a 0%, #a39a4e 30%, #4c5a2a 65%, #2b3418 100%);
  }
  .map {
    position: absolute; left: 0; top: 0; width: 100%; height: 250px;
    background: linear-gradient(135deg, #e6e3dc, #d9e6cf 55%, #e8e5de);
  }

  .swoosh { position: absolute; left: 0; width: 100%; height: 90px; }
  .panel--story .swoosh { top: 250px; }
  .panel--cover .swoosh { top: 320px; }

  .story { position: absolute; left: 40px; right: 34px; top: 360px; }
  .story__title {
    font-family: "Didact Gothic", sans-serif;
    font-size: 24px; color: var(--ink);
    margin-bottom: 14px;
  }
  .story__body {
    font-size: 14px; line-height: 1.55; text-align: justify; color: var(--ink-soft);
  }

  .agency {
    position: absolute; left: 40px; right: 40px; top: 330px;
    display: flex; align-items: center; gap: 10px;
  }
  .agency__mark { width: 16px; height: 16px; background: var(--green); flex: none; }
  .agency__name {
    font-family: "Lato", sans-serif; font-weight: 700;
    font-size: 15px; letter-spacing: .04em; text-transform: uppercase;
    color: var(--green-deep); line-height: 1.3;
  }
  .contact {
    position: absolute; left: 40px; right: 40px; top: 450px;
    text-align: center; font-size: 15px; line-height: 1.45; color: var(--ink);
  }
  .contact__role { margin-bottom: 22px; }

  .tagline {
    position: absolute; left: 150px; top: 30px;
    color: #fff; font-family: "Lato", sans-serif; font-weight: 300;
    font-size: 38px; line-height: .95;
  }
  .development {
    position: absolute; left: 0; right: 0; top: 430px; text-align: center;
  }
  .development__name {
    display: inline-flex; align-items: center; gap: 10px;
    font-family: "Montserrat", sans-serif; font-weight: 700;
    font-size: 30px; color: var(--ink); letter-spacing: .02em;
  }
  .development__mark { width: 18px; height: 18px; border-radius: 50%; background: var(--orange); }
  .offer {
    position: absolute; left: 40px; top: 520px;
    display: flex; align-items: center; gap: 16px;
  }
  .offer__count { font-weight: 300; font-size: 88px; line-height: 1; color: var(--ink); }
  .offer__detail { font-weight: 300; font-size: 21px; line-height: 1.15; color: var(--ink-soft); }
  .cover-band {
    position: absolute; left: 0; right: 0; bottom: 0; height: 110px;
    background: linear-gradient(180deg, #ececec, var(--band-grey));
    display: flex; flex-direction: column; justify-content: center;
    padding: 0 28px;
    font-size: 22px; font-weight: 400; line-height: 1.15; color: var(--ink);
    text-transform: uppercase;
  }
</style>
</head>
<body>
<main class="brochure">
  <section class="panel panel--story">
    <div class="photo photo--entrance" role="img" aria-label="Photo of the site entrance with gum trees and the Kennel Haven gate sign"></div>
    <svg class="swoosh" viewBox="0 0 340 90" preserveAspectRatio="none" aria-hidden="true">
      <path d="M0 0 H340 V50 Q170 0 0 60 Z" fill="var(--green)"/>
      <path d="M0 60 Q170 0 340 50 V62 Q170 14 0 74 Z" fill="var(--orange)"/>
      <path d="M0 74 Q170 14 340 62 V90 H0 Z" fill="var(--paper)"/>
    </svg>
    <article class="story">
      <h2 class="story__title">Sed bibendum vitae</h2>
      <p class="story__body">Suspendisse cursus ipsum in mauris mattis, eget imperdiet nibh dapibus. Phasellus faucibus turpis at ipsum sagittis placerat. Duis aliquet gravida felis at consequat. Etiam sit amet velit consectetur, blandit ante sed, gravida sem. Sed bibendum vitae velit nec consequat. Aliquam dignissim semper nunc non imperdiet magna aliquam eget. Maecenas in nibh vitae massa</p>
    </article>
  </section>

  <section class="panel panel--contact">
    <div class="map" role="img" aria-label="Street map showing 2847 Silverfern Crescent Road, Greenwith"></div>
    <div class="agency">
      <span class="agency__mark" aria-hidden="true"></span>
      <span class="agency__name">Harlow Reid Real Estate<br>&amp; Coastline Property Rentals</span>
    </div>
    <address class="contact" style="font-style:normal">
      <p>Sam Harlow</p>
      <p class="contact__role">Director</p>
      <p>P: 0400 555 182</p>
      <p>F: (08) 7000 4816</p>
      <p>E: sam@coastlinerentals.com.au</p>
      <p>A: PO Box 220, Northfield SA 5085</p>
      <p>Suite 8, 45 Marlow St.</p>
      <p>Northfield SA 5085</p>
    </address>
  </section>

  <section class="panel panel--cover">
    <div class="photo photo--meadow" role="img" aria-label="Sunlit meadow of wildflowers at golden hour"></div>
    <p class="tagline">live<br>your<br>life<br>naturally</p>
    <svg class="swoosh" viewBox="0 0 340 90" preserveAspectRatio="none" aria-hidden="true">
      <path d="M0 0 H340 V40 Q170 10 0 45 Z" fill="var(--green)"/>
      <path d="M0 45 Q170 10 340 40 V54 Q170 24 0 58 Z" fill="var(--orange)"/>
      <path d="M0 58 Q170 24 340 54 V90 H0 Z" fill="var(--paper)"/>
    </svg>
    <div class="development">
      <h1 class="development__name"><span class="development__mark" aria-hidden="true"></span>THE WATTLEBROOK</h1>
    </div>
    <div class="offer">
      <span class="offer__count">14</span>
      <span class="offer__detail">Premium<br>Allotments<br>Greenwith</span>
    </div>
    <div class="cover-band">
      <span>Lorem ipsum dolor sit</span>
      <span>Consectetur adipiscing</span>
    </div>
  </section>
</main>
</body>
</html>
```